General contractor/GM consaltant business card

I need a card for my contracting company in North Dakota, we build industrial buildings for the oil feild and oil feild related companies offices, shops, airplain hangars, airports ext. We have a familly atmosphere on the job and are very relational and personal.
Industry/Entity Type
Industrial
Contact Information for Business Card
Hollowpine Crafters LLC.
Dale T.Voskuijl
4873 Quenwick dr. Colorado Springs, CO. 80462
Cell# 406-738-1452
dale@hollowpinecrafters.example

```html
<!DOCTYPE html>
<html lang="en">
<head>
<meta charset="utf-8">
<title>Hollowpine Crafters LLC – Business Card</title>
<link rel="stylesheet" href="https://fonts.googleapis.com/css2?family=Tinos:wght@400&family=Montserrat:wght@400;500&display=swap">
<style>
  :root {
    --page: #f4f5f7;
    --navy-deep: #0d1222;
    --navy: #1a2238;
    --navy-soft: #2a3452;
    --paper: #eceef0;
    --paper-shade: #d9dcdf;
    --silver: #c9ccd2;
    --silver-light: #f2f3f5;
    --ink: #1e2a4a;
    --ink-soft: #4a5266;
    --text-light: #e8eaee;
    --text-muted: #aeb4c2;
  }
  * { box-sizing: border-box; margin: 0; padding: 0; }
  html, body { width: 1200px; height: 900px; overflow: hidden; }
  body {
    background: var(--page);
    font-family: "Tinos", "Times New Roman", serif;
    position: relative;
  }
  .card {
    position: absolute;
    top: 295px;
    width: 540px;
    height: 310px;
    border-radius: 24px;
    overflow: hidden;
    box-shadow: 0 14px 30px rgba(20, 26, 45, 0.28);
  }
  .card--front { left: 40px; }
  .card--back { left: 620px; }

  /* Front */
  .front-surface {
    position: absolute; inset: 0;
    background: radial-gradient(ellipse at 50% 35%, var(--navy-soft) 0%, var(--navy) 45%, var(--navy-deep) 100%);
  }
  .front-brand {
    position: absolute; left: 0; right: 0; top: 72px;
    display: flex; flex-direction: column; align-items: center;
  }
  .brand-square {
    width: 84px; height: 84px;
    border-radius: 12px;
    background: linear-gradient(180deg, var(--navy-soft), var(--navy-deep));
    border: 2px solid var(--silver);
  }
  .front-name {
    margin-top: 16px;
    font-size: 31px;
    color: var(--silver);
    letter-spacing: 0.3px;
  }
  .front-rule {
    width: 268px; height: 1px;
    margin-top: 6px;
    background: var(--text-muted);
  }
  .tagline {
    font-family: "Montserrat", Arial, sans-serif;
    font-size: 10.5px;
    letter-spacing: 2.2px;
    text-transform: uppercase;
  }
  .front-tagline { margin-top: 6px; color: var(--text-muted); }

  /* Back */
  .back-top {
    position: absolute; left: 0; top: 0; width: 100%; height: 150px;
    background: linear-gradient(160deg, var(--silver-light) 0%, var(--paper) 55%, var(--paper-shade) 100%);
  }
  .back-band {
    position: absolute; left: 0; top: 150px; width: 100%; height: 8px;
    background: linear-gradient(90deg, #8e929a 0%, var(--silver-light) 45%, #9ea2aa 100%);
  }
  .back-bottom {
    position: absolute; left: 0; top: 158px; width: 100%; height: 152px;
    background: linear-gradient(180deg, var(--navy) 0%, var(--navy-deep) 100%);
  }
  .back-brand {
    position: absolute; left: 26px; top: 30px;
    display: flex; align-items: center;
  }
  .back-brand .brand-square { width: 96px; height: 96px; }
  .back-brand-text { margin-left: 14px; }
  .back-name {
    font-size: 27px;
    color: var(--ink);
    white-space: nowrap;
  }
  .back-rule {
    width: 262px; height: 1px;
    margin-top: 5px;
    background: var(--ink-soft);
  }
  .back-tagline { margin-top: 5px; color: var(--ink-soft); font-size: 9.5px; }

  .person {
    position: absolute; left: 30px; top: 168px;
  }
  .person-name {
    font-size: 21px;
    color: var(--silver);
    letter-spacing: 0.4px;
  }
  .person-title {
    font-size: 13px;
    color: var(--text-light);
    margin-top: 1px;
  }
  .contact-list {
    list-style: none;
    margin-top: 10px;
    color: var(--text-light);
    font-size: 15px;
    line-height: 19px;
  }
  .contact-list li { display: flex; align-items: flex-start; }
  .contact-icon { width: 14px; height: 14px; margin: 2px 5px 0 0; flex: none; }
  .contact-indent { padding-left: 19px; }
</style>
</head>
<body>

  <section class="card card--front" aria-label="Card front">
    <div class="front-surface" role="img" aria-label="Dark navy finish with fine texture"></div>
    <div class="front-brand">
      <div class="brand-square"></div>
      <div class="front-name">Hollowpine Crafters LLC.</div>
      <div class="front-rule"></div>
      <div class="tagline front-tagline">General Contractor/GM Consultant</div>
    </div>
  </section>

  <section class="card card--back" aria-label="Card back">
    <div class="back-top" role="img" aria-label="Light paper texture"></div>
    <div class="back-band"></div>
    <div class="back-bottom"></div>

    <div class="back-brand">
      <div class="brand-square"></div>
      <div class="back-brand-text">
        <div class="back-name">Hollowpine Crafters LLC.</div>
        <div class="back-rule"></div>
        <div class="tagline back-tagline">General Contractor/GM Consultant</div>
      </div>
    </div>

    <div class="person">
      <div class="person-name">Dale T.Voskuijl</div>
      <div class="person-title">Director</div>
      <ul class="contact-list">
        <li>
          <svg class="contact-icon" viewBox="0 0 14 14" aria-hidden="true">
            <rect x="3.5" y="1" width="7" height="12" rx="1.2" fill="var(--text-light)"/>
            <rect x="4.8" y="2.5" width="4.4" height="7" fill="var(--navy)"/>
          </svg>
          406-738-1452
        </li>
        <li>
          <svg class="contact-icon" viewBox="0 0 14 14" aria-hidden="true">
            <rect x="1" y="3" width="12" height="8.5" rx="1" fill="var(--text-light)"/>
            <polyline points="1.5,3.6 7,8 12.5,3.6" fill="none" stroke="var(--navy)" stroke-width="1.2"/>
          </svg>
          dale@hollowpinecrafters.example
        </li>
        <li>
          <svg class="contact-icon" viewBox="0 0 14 14" aria-hidden="true">
            <polygon points="7,1.5 13,7 11.3,7 11.3,12.5 8.3,12.5 8.3,9 5.7,9 5.7,12.5 2.7,12.5 2.7,7 1,7" fill="var(--text-light)"/>
          </svg>
          4873 Quenwick dr.
        </li>
        <li class="contact-indent">Colorado Springs, CO. 80462</li>
      </ul>
    </div>
  </section>

</body>
</html>
```